The hardcover "Velvet Register" (large size, Quarto 4º, 12 × 9 1/2 in, 30.5 × 24.15 cm) in German language as follows:

SAMTENES REGISTER (title)
der bemerkenswertesten Gründer und Führungskräfte im Norden 2014 (subtitle 1)
HAFEN UND MARSCHLAND (subtitle 2, smaller than subtitle 1)

Korvalix (logo, WMF file attached)

Reason: The solutions are rather too childish and pre-made styles... is there anyone who can make it better? - a professional-looking business book (encyclopedia style, should have no color-pictures, no author's name, logo smaller due to the large size book)

Target Market(s)

business community

Requirements
Must have
• encyclopedia style large size book
must look professional and expensive

Nice to have
• - gold-color hardcover, or some gold-color elements
- some simple and decent graphic element (e.g. an ancient column, or some other architectural detail), if any
Should not have
• no color-pictures
no author's name

```html
<!DOCTYPE html>
<html lang="de">
<head>
<meta charset="utf-8">
<title>Samtenes Register</title>
<link rel="stylesheet" href="https://fonts.googleapis.com/css2?family=Jost:wght@300;400;700&display=swap">
<style>
  :root {
    --cover: #7f6c00;
    --band: #776400;
    --band-shadow: rgba(40, 33, 0, 0.6);
    --title-fill: #6c5a00;
    --title-line: #cdb51e;
    --text-light: #f6f1dc;
    --brand: #9b8600;
  }
  html, body {
    margin: 0;
    padding: 0;
    overflow: hidden;
  }
  .cover {
    position: relative;
    width: 954px;
    height: 1200px;
    background: var(--cover);
    overflow: hidden;
  }
  .title-band {
    position: absolute;
    left: 57px;
    top: 261px;
    width: 897px;
    height: 200px;
    background: var(--band);
    box-shadow: 0 6px 8px var(--band-shadow);
  }
  .subtitle-band {
    position: absolute;
    left: 0;
    top: 514px;
    width: 908px;
    height: 139px;
    background: var(--band);
    box-shadow: 0 5px 7px var(--band-shadow);
  }
  .band-text {
    position: absolute;
    left: 0;
    top: 0;
    display: block;
  }
  .title {
    font-family: "Jost", sans-serif;
    font-weight: 700;
    font-size: 86px;
    fill: var(--title-fill);
    stroke: var(--title-line);
    stroke-width: 1.6px;
    filter: drop-shadow(2px 3px 2px rgba(40, 33, 0, 0.5));
  }
  .subtitle {
    font-family: "Jost", sans-serif;
    font-weight: 300;
    font-size: 31px;
    fill: var(--text-light);
  }
  .region {
    font-family: "Jost", sans-serif;
    font-weight: 400;
    font-size: 21px;
    fill: var(--text-light);
  }
  .brand {
    position: absolute;
    right: 40px;
    bottom: 48px;
    display: flex;
    align-items: center;
    gap: 14px;
  }
  .brand-mark {
    width: 22px;
    height: 22px;
    background: var(--brand);
  }
  .brand-name {
    font-family: "Jost", sans-serif;
    font-weight: 700;
    font-size: 86px;
    line-height: 1;
    color: var(--brand);
  }
</style>
</head>
<body>
  <main class="cover">
    <section class="title-band">
      <svg class="band-text" width="897" height="200" viewBox="0 0 897 200">
        <text class="title" x="46" y="134" textLength="792" lengthAdjust="spacingAndGlyphs">SAMTENES REGISTER</text>
      </svg>
    </section>
    <section class="subtitle-band">
      <svg class="band-text" width="908" height="139" viewBox="0 0 908 139">
        <text class="subtitle" x="60" y="66" textLength="804" lengthAdjust="spacingAndGlyphs">der bemerkenswertesten Gründer und Führungskräfte im Norden 2014</text>
        <text class="region" x="862" y="108" text-anchor="end" textLength="236" lengthAdjust="spacingAndGlyphs">HAFEN UND MARSCHLAND</text>
      </svg>
    </section>
    <div class="brand">
      <span class="brand-mark"></span>
      <span class="brand-name">Korvalix</span>
    </div>
  </main>
</body>
</html>
```